Publishing company needs book cover for multi-author book

Copperfield Lane Publishing needs a book cover designed for a multi-author book called Harbor Lanterns: Unlikely Triumph Accounts from Remarkable Pioneers. We would like to see designs that incorporates the design theme of the image attached and possibly the image itself. The book will be used by the contributing authors who are  are Healers, Psychics, Coaches, Energy Workers, Astrologers, Numerologist, Tarot Card Readers and will be using this book to both market their business and use in their practices.  The final design should communicate  these spiritual practices.
I would love to see
1. A silhouette or image of a woman holding a ball or circle with the attached art inside of.
2. The concepts in the attached art brought into a  new design or  enhancing the original art.

Target Market(s)
The clients and audiences of the contributing authors
Industry/Entity Type
Spiritual, Body Mind Spirit, Evolving Continuousness, Alternative Healing
Colors
Designer to choose colors to be used in the design.
Requirements
Must have
- Title- Harbor Lanterns: Unlikely Triumph Accounts from Remarkable Pioneers. and the name of the publishing company: Copperfield Lane Publishing

Nice to have
- I would love to have the concept of the artwork coming to life through an image of woman, visionary, healer who is healing the world through her modalities.

Should not have
- Dimensions - 6X9

```html
<!DOCTYPE html>
<html lang="en">
<head>
<meta charset="utf-8">
<title>Harbor Lanterns – Book Cover</title>
<link rel="stylesheet" href="https://fonts.googleapis.com/css2?family=Playfair+Display:wght@500&family=Poppins:wght@600;700&display=swap">
<style>
  :root {
    --stage: #1c1618;
    --gold: #d4962c;
    --white: #ffffff;
    --sky: #8cc4e8;
    --deep-blue: #2c5a92;
    --night: #2b2a35;
    --earth: #5a3b2a;
    --moss: #5d7a3a;
  }
  html, body {
    margin: 0;
    padding: 0;
    width: 1200px;
    height: 1200px;
    overflow: hidden;
    background: var(--stage);
  }
  .canvas {
    position: relative;
    width: 1200px;
    height: 1200px;
    background: var(--stage);
  }
  .book-cover {
    position: absolute;
    left: 255px;
    top: 82px;
    width: 690px;
    height: 1036px;
    overflow: hidden;
  }
  .cover-artwork {
    position: absolute;
    inset: 0;
    background:
      radial-gradient(circle at 56% 48%, #d9ecf8 0%, var(--sky) 12%, #6f4a35 20%, var(--earth) 26%, var(--sky) 34%, #b8d9ef 44%, var(--night) 56%, #1f2030 72%, var(--deep-blue) 100%),
      var(--night);
  }
  .cover-artwork::after {
    content: "";
    position: absolute;
    inset: 0;
    background:
      linear-gradient(180deg, rgba(60,80,150,0.35) 0%, rgba(0,0,0,0) 30%),
      linear-gradient(0deg, rgba(200,110,40,0.35) 0%, rgba(93,122,58,0.2) 18%, rgba(0,0,0,0) 35%);
  }
  .publisher-tab {
    position: absolute;
    left: 0;
    top: 0;
    width: 53px;
    height: 268px;
    background: var(--gold);
  }
  .publisher-name {
    position: absolute;
    left: 26.5px;
    top: 134px;
    transform: translate(-50%, -50%) rotate(-90deg);
    white-space: nowrap;
    font-family: "Poppins", sans-serif;
    font-weight: 600;
    font-size: 15px;
    color: var(--white);
    margin: 0;
  }
  .book-title {
    position: absolute;
    left: 378px;
    top: 1088px;
    transform-origin: top left;
    transform: rotate(-90deg);
    margin: 0;
    font-family: "Playfair Display", serif;
    font-weight: 500;
    font-size: 196px;
    line-height: 200px;
    color: var(--white);
    white-space: nowrap;
  }
  .title-line {
    display: block;
  }
  .title-line--second {
    padding-left: 182px;
  }
  .book-subtitle {
    position: absolute;
    left: 620px;
    top: 948px;
    margin: 0;
    font-family: "Poppins", sans-serif;
    font-weight: 700;
    font-size: 27px;
    line-height: 34px;
    color: var(--white);
  }
</style>
</head>
<body>
  <main class="canvas">
    <section class="book-cover">
      <div class="cover-artwork" role="img" aria-label="Painted spiral artwork of sky, birds, earth, ocean, moon phases, feathers and a mandala swirling around a central eye"></div>
      <div class="publisher-tab">
        <p class="publisher-name">Copperfield Lane Publishing</p>
      </div>
    </section>
    <h1 class="book-title">
      <span class="title-line">Harbor</span>
      <span class="title-line title-line--second">Lanterns</span>
    </h1>
    <p class="book-subtitle">Unlikely Triumph<br>Accounts from<br>Remarkable<br>Pioneers</p>
  </main>
</body>
</html>
```